Business Card Design Project- Removalist

I would like to surprise my husband to be with a different type of wedding present. His brother (who he owned a removalist business with) suddenly passed away from cancer recently and he has changed his business name to 'RTB' (which stands for Raising Tom Bright; but the full name doesn't need to be on the business card as it is more of a personal business name). To celebrate the new business I would like to get him some business cards made.
I would like the business name to be listed as 'RTB' and somewhere on the card I would like 'Sydney wide removals and relocation services'. I would like it to be obvious from the front of the card that it is a removalist business card. If a truck or some other feature that makes it look like a removalist business card could added it would be appreciated.
I don't mind what colours are used, but I would like the colour blue to feature somewhere in the design. It can be bright and fun, which is how Tom was.
I will also need the company's email address and phone number listed
The email address is: rtbremovals@quillpost.example
The contact number is: 0417 282 934
I don't need a contact name listed on the card, but perhaps 'Owned and operated by the Pendleworth family' could be added near the contact details in small font.
Thank you very much for considering this project!
Kind regards,
Fiona
Updates
Could you please change the mobile contact number to 0417 282 934. This is the only contact phone number required on the card now.
Thank you!

```html
<!DOCTYPE html>
<html lang="en">
<head>
<meta charset="utf-8">
<title>RTB Removals – Business Card</title>
<link rel="stylesheet" href="https://fonts.googleapis.com/css2?family=Oswald:wght@400;700&display=swap">
<style>
  :root {
    --navy: #2b3990;
    --sky: #3fa9e0;
    --mid-blue: #2f7fc6;
    --lime: #8dc63f;
    --white: #ffffff;
    --ink: #27306f;
    --grey: #555a66;
    --stage: #eef0f3;
  }
  html, body {
    margin: 0;
    padding: 0;
    width: 1200px;
    height: 854px;
    overflow: hidden;
    background: var(--stage);
  }
  .card {
    position: relative;
    width: 1200px;
    height: 854px;
    background: var(--white);
    font-family: "Oswald", "Arial Narrow", sans-serif;
    overflow: hidden;
  }
  .tagline {
    position: absolute;
    top: 26px;
    left: 0;
    width: 100%;
    text-align: center;
    margin: 0;
    font-weight: 700;
    font-size: 52px;
    letter-spacing: 0.5px;
    color: var(--ink);
    text-transform: uppercase;
    line-height: 1;
  }
  .tagline .accent { color: var(--sky); }
  .ownership {
    position: absolute;
    top: 94px;
    left: 0;
    width: 100%;
    text-align: center;
    margin: 0;
    font-weight: 400;
    font-size: 22px;
    color: var(--grey);
  }
  .ownership .family { text-transform: uppercase; font-weight: 700; }
  .brand {
    position: absolute;
    top: 135px;
    left: 0;
    width: 100%;
    height: 410px;
    display: flex;
    align-items: center;
    justify-content: center;
    gap: 40px;
  }
  .brand-name {
    font-weight: 700;
    font-size: 330px;
    line-height: 1;
    color: var(--mid-blue);
    letter-spacing: 6px;
  }
  .brand-dot {
    width: 70px;
    height: 70px;
    border-radius: 50%;
    background: var(--sky);
    align-self: flex-end;
    margin-bottom: 40px;
  }
  .contact-strip {
    position: absolute;
    left: 0;
    top: 560px;
    width: 100%;
    height: 20px;
    background: var(--sky);
  }
  .contact-band {
    position: absolute;
    left: 0;
    top: 580px;
    width: 100%;
    height: 274px;
    box-sizing: border-box;
    padding: 0 48px;
    background: var(--navy);
    display: flex;
    align-items: center;
    justify-content: space-between;
    gap: 40px;
  }
  .call-us {
    margin: 0;
    font-weight: 700;
    font-size: 112px;
    line-height: 1;
    color: var(--lime);
    text-transform: uppercase;
    white-space: nowrap;
  }
  .contact-details {
    display: flex;
    flex-direction: column;
    align-items: flex-end;
    gap: 14px;
  }
  .phone {
    margin: 0;
    font-weight: 700;
    font-size: 100px;
    line-height: 1;
    color: var(--white);
    letter-spacing: 2px;
    white-space: nowrap;
  }
  .email {
    margin: 0;
    font-weight: 400;
    font-size: 34px;
    line-height: 1;
    color: var(--white);
    white-space: nowrap;
  }
</style>
</head>
<body>
  <main class="card">
    <h1 class="tagline">Sydney <span class="accent">wide</span> removals &amp; relocation services</h1>
    <p class="ownership">Owned and operated by the <span class="family">Pendleworth</span> family</p>

    <div class="brand">
      <span class="brand-name">RTB</span>
      <span class="brand-dot" aria-hidden="true"></span>
    </div>

    <div class="contact-strip" aria-hidden="true"></div>
    <section class="contact-band">
      <p class="call-us">Call us!</p>
      <div class="contact-details">
        <p class="phone">0417 282 934</p>
        <p class="email">rtbremovals@quillpost.example</p>
      </div>
    </section>
  </main>
</body>
</html>
```